Visitenkartenerstellung für Dorvek-Estates
Zielgruppe
Männer und Frauen, junge Familien bis hin zum Senior.
Verkauf von hochwertigen Immobilien in Spanien.
Aufgabenstellung
Auf Grund unserer Namensänderung benötigen wir ein neues Visitenkartendesign.
Wir sind eine skandinavische Agentur für Luxus-Immobilien auf Mallorca.
Das Design sollte dementsprechend edel aber dennoch schlicht gestaltet sein!

```html
<!DOCTYPE html>
<html lang="en">
<head>
<meta charset="utf-8">
<title>Dorvek-Estates – Business Card</title>
<link rel="stylesheet" href="https://fonts.googleapis.com/css2?family=Lato:wght@300;400;700&display=swap">
<style>
  :root {
    --backdrop: #ececec;
    --card: #ffffff;
    --card-edge: #4a4a4a;
    --ink-strong: #262626;
    --ink: #404040;
    --ink-soft: #555555;
  }
  * { margin: 0; padding: 0; box-sizing: border-box; }
  html, body {
    width: 1200px;
    height: 754px;
    overflow: hidden;
    background: var(--backdrop);
    font-family: "Lato", "Helvetica Neue", Arial, sans-serif;
  }
  .sheet {
    position: relative;
    width: 1200px;
    height: 754px;
  }
  .card {
    position: absolute;
    width: 484px;
    height: 312px;
    background: var(--card);
    border: 1px solid var(--card-edge);
  }
  .card--front { left: 140px; top: 120px; }
  .card--back  { left: 640px; top: 330px; }

  .brand {
    position: absolute;
    left: 80px;
    top: 108px;
    font-weight: 400;
    font-size: 44px;
    line-height: 1;
    letter-spacing: -0.3px;
    color: var(--ink-strong);
    white-space: nowrap;
  }
  .tagline {
    position: absolute;
    left: 81px;
    top: 178px;
    font-weight: 400;
    font-size: 16.5px;
    color: var(--ink);
    white-space: nowrap;
  }

  .contact {
    position: absolute;
    left: 109px;
    top: 64px;
    color: var(--ink);
    font-size: 15.5px;
    line-height: 24px;
  }
  .contact__head { margin-bottom: 10px; white-space: nowrap; }
  .contact__name {
    font-weight: 700;
    font-size: 17px;
    color: var(--ink-strong);
    margin-right: 5px;
  }
  .contact__role {
    font-weight: 400;
    font-size: 15px;
    color: var(--ink-soft);
  }
  .contact__group { margin-bottom: 12px; font-weight: 400; }
</style>
</head>
<body>
  <main class="sheet">
    <section class="card card--front" aria-label="Card front">
      <div class="brand">Dorvek-Estates.com</div>
      <p class="tagline">Luxury Real Estate on Mallorca &amp; Ibiza</p>
    </section>

    <section class="card card--back" aria-label="Card back">
      <div class="contact">
        <p class="contact__head">
          <span class="contact__name">Karin Lindqvist</span>
          <span class="contact__role">Property Manager</span>
        </p>
        <p class="contact__group">C. Almendro 12<br>07190 Portals Spain</p>
        <p class="contact__group">Tel. 971555018<br>Mobil 0034 60055512</p>
        <p class="contact__group">Karin.Lindqvist@dorvek-estates.com<br>www.dorvek-estates.se</p>
      </div>
    </section>
  </main>
</body>
</html>
```